BorrowNest Website design, we are a home loan / lending company

We are a finance broking company that can do mortgages / home loans, Car Loans, Commercial Loans, SMSF Loans, Business Loans, Personal Loans
We are looking for a simple website, not too busy, easy to navigate, something that prompts customers to action or call us.
I like the simplicity of the following websites:
https://www.veltronacapital.com.au/ - I like this website front page. I was thinking I have my logo, the one with the black background appear , then the toolbar at the top perhaps?
https://zendira.com.au/business-loans# - on this page there are images under finance that works for you that I like that concept.
https://quillmark.com.au/contact/ - I like the Make an Appointment page
https://zendira.com.au/about-us - Simple but effective page design

Target Market(s)

Home Loan Customer

Industry/Entity Type

Finance / Home Loans

Coding

Coded - Design and coding required

Number of Pages Required

5+ page

Font styles to use
Serif

Colors
0094D4
00A9DD
6FCCEA
C7EBF8
E9F6FB

Requirements
Must have
• The following Heading s - Contact Us, About Us, Our People, Make an Appointment, Loan Options, Calculators, Reviews. I want to use the Logo colours I have in the zip files I uploaded.
Nice to have
• Simple clean design

```html
<!DOCTYPE html>
<html lang="en">
<head>
<meta charset="utf-8">
<title>BorrowNest – Finance Broking</title>
<link rel="stylesheet" href="https://fonts.googleapis.com/css2?family=Poppins:wght@400;500;600;700&display=swap">
<style>
:root{
  --blue:#0094D4;
  --blue-2:#00A9DD;
  --blue-3:#6FCCEA;
  --blue-4:#C7EBF8;
  --blue-5:#E9F6FB;
  --deep:#0a7bd0;
  --ink:#222;
  --text:#4a4a4a;
  --card:#f6f7f9;
  --black:#111214;
  --black-2:#0b0b0c;
  --star:#ffc515;
}
*{box-sizing:border-box;margin:0;padding:0}
html,body{width:1200px;height:5164px;overflow:hidden}
body{position:relative;font-family:"Poppins",sans-serif;color:var(--ink);background:#fff}
.abs{position:absolute}
a{color:inherit;text-decoration:none}

/* header */
.brand{font-family:"Poppins",sans-serif;font-weight:600;letter-spacing:-1px}
.site-header .brand{left:74px;top:30px;font-size:40px;color:#2a2a2a}
.btn-outline{left:602px;top:26px;width:198px;height:58px;border:2px solid var(--blue);border-radius:3px;
  color:var(--blue);font-weight:600;font-size:19px;display:flex;align-items:center;justify-content:center}
.header-phone{left:910px;top:40px;font-weight:600;font-size:20px;color:#2a2a2a;display:flex;align-items:center;gap:12px}
.main-nav{left:0;top:108px;width:1200px;height:60px;background:var(--blue);display:flex;align-items:center;padding-left:98px;gap:0}
.main-nav a{color:#fff;font-weight:600;font-size:18px;margin-right:56px}

/* hero */
.hero-photo{left:0;top:168px;width:1200px;height:840px;
  background:linear-gradient(100deg,#6a6660 0%,#8b8278 30%,#a9a39a 55%,#5c5d63 80%,#3e4150 100%)}
.hero-shade{left:0;top:168px;width:1200px;height:840px;background:rgba(0,0,0,.18)}
.hero-title{left:0;width:1200px;text-align:center;color:#fff;font-weight:700}
.hero-title.t1{top:262px;font-size:60px}
.hero-title.t2{top:322px;font-size:80px;letter-spacing:-1px}
.hero-sub{left:0;top:424px;width:1200px;text-align:center;color:#fff;font-weight:600;font-size:32px}
.btn-solid{background:var(--blue-3);color:#fff;font-weight:600;display:flex;align-items:center;justify-content:center}
.hero-btn{left:502px;top:494px;width:196px;height:50px;font-size:18px}
.dots{left:544px;top:714px;display:flex;gap:16px}
.dots i{width:14px;height:14px;border-radius:50%;background:#fff}
.dots i:first-child{background:var(--blue)}

/* backdrop */
.backdrop{left:0;top:860px}

/* loan options */
.loan-card{left:74px;top:796px;width:1052px;height:740px;background:var(--card);box-shadow:0 4px 14px rgba(0,0,0,.12)}
.section-title{font-weight:700;font-size:44px;text-align:center;color:var(--ink)}
.section-lead{font-size:15px;line-height:26px;text-align:center;color:var(--text)}
.loan-card .section-title{position:absolute;left:0;top:32px;width:100%}
.loan-card .section-lead{position:absolute;left:40px;top:104px;width:972px}
.loan-grid{left:32px;top:200px;width:990px;height:490px;display:grid;grid-template-columns:328px 334px 328px;grid-template-rows:248px 242px}
.loan-item{text-align:center;padding-top:18px;border-right:1px solid #d3d6da;border-bottom:1px solid #d3d6da}
.loan-item:nth-child(3n){border-right:none}
.loan-item:nth-child(n+4){border-bottom:none}
.loan-item.is-active{background:#fff;box-shadow:0 2px 10px rgba(0,0,0,.18);border:none}
.loan-item.is-active h3{color:var(--blue)}
.loan-item svg{display:block;margin:0 auto 6px}
.loan-item h3{font-size:21px;font-weight:600;margin-bottom:8px}
.loan-item p{font-size:14.5px;line-height:26px;color:var(--text);padding:0 26px}

/* about */
.about-photo{left:74px;top:1640px;width:512px;height:426px;border-radius:4px;
  background:linear-gradient(120deg,#d9d2c8 0%,#b49a82 40%,#7b6655 70%,#3d3a3a 100%)}
.about-title{left:614px;top:1636px;color:#fff;font-weight:700;font-size:42px;line-height:46px}
.about-text{left:614px;top:1748px;width:500px;color:#fff;font-size:16px;line-height:33px}
.about-btn{left:614px;top:2012px;width:194px;height:50px;font-size:18px}

/* people */
.people .section-title{position:absolute;left:0;top:2204px;width:1200px}
.people .section-lead{position:absolute;left:120px;top:2276px;width:960px}
.person{top:2410px;width:242px;height:334px;border-radius:10px;background:var(--blue-5);text-align:center;padding-top:140px}
.person.is-active{background:#fff;box-shadow:0 6px 18px rgba(0,0,0,.16)}
.person .avatar{position:absolute;left:39px;top:-48px;width:164px;height:164px;border-radius:50%;
  background:linear-gradient(160deg,#e8eaec,#9aa2ab);border:3px solid #fff}
.person h4{font-size:19px;font-weight:600;margin-bottom:6px}
.person p{font-size:15px;line-height:26px;color:var(--text);padding:0 18px}
.person svg{margin-top:10px}

/* reviews */
.reviews{left:0;top:2832px;width:1200px;height:444px;
  background:linear-gradient(105deg,#0f6fc7 0%,#1a86d6 45%,#38a8e2 75%,#63c2ea 100%)}
.reviews .section-title{position:absolute;left:0;top:74px;width:100%;color:#fff}
.review{top:162px;width:320px;color:#fff}
.review .avatar{width:88px;height:88px;border-radius:50%;background:linear-gradient(160deg,#f1f1f1,#8a96a3);position:absolute;left:0;top:0}
.review .stars{position:absolute;left:104px;top:10px;display:flex;gap:6px}
.review h5{position:absolute;left:104px;top:40px;font-size:19px;font-weight:600;white-space:nowrap}
.review p{position:absolute;left:0;top:108px;width:320px;font-size:14.5px;line-height:27px}

/* steps */
.steps-title{left:0;top:3324px;width:1200px;text-align:center;font-weight:700;font-size:42px}
.step-btn{top:3436px;width:242px;height:80px;border-radius:6px;background:var(--blue);color:#fff;font-weight:600;font-size:26px;display:flex;justify-content:center;padding-top:18px}
.step-num{top:3496px;width:44px;height:44px;border-radius:50%;background:var(--blue-3);border:3px solid #fff;color:#fff;font-weight:600;font-size:20px;display:flex;align-items:center;justify-content:center}
.step-text{top:3722px;width:320px;text-align:center;font-size:17px;line-height:30px;color:var(--text)}

/* appointment */
.appointment{left:0;top:3864px;width:1200px;height:760px;background:var(--blue-5)}
.appointment .section-title{position:absolute;left:0;top:80px;width:100%}
.appointment .section-lead{position:absolute;left:150px;top:156px;width:900px;font-size:16.5px;line-height:32px}
.field{width:426px;height:58px;background:#fff;border:1px solid #dde3e6;font-size:15px;color:#333;padding-left:16px;display:flex;align-items:center}
.submit{width:426px;height:58px;background:var(--blue);color:#fff;font-weight:600;font-size:18px;display:flex;align-items:center;justify-content:center}

/* footer */
.footer-base{left:0;top:4470px}
.site-footer .brand{left:74px;top:4592px;font-size:50px;color:#fff}
.news-label{left:560px;top:4590px;color:#fff;font-weight:500;font-size:18px}
.news-input{left:560px;top:4628px;width:406px;height:48px;background:#fff;font-size:14px;padding-left:16px;display:flex;align-items:center}
.news-btn{left:976px;top:4628px;width:150px;height:48px;background:var(--blue);color:#fff;font-weight:600;font-size:18px;display:flex;align-items:center;justify-content:center}
.footer-rule{left:0;top:4700px;width:1200px;height:1px;background:#2d2f33}
.f-col h6{color:#fff;font-size:21px;font-weight:600;margin-bottom:14px}
.f-col li{list-style:none;color:#d8d8d8;font-size:14.5px;line-height:35px}
.socials{display:flex;gap:22px;margin-top:6px}
.socials i{width:22px;height:22px;border-radius:4px;background:#fff;display:block}
.f-contact{color:var(--blue-2);font-size:18px;display:flex;align-items:center;gap:14px;margin-top:14px}
.copyright{left:0;top:5080px;width:1200px;height:84px;background:var(--black-2);color:#d0d0d0;font-size:14px;display:flex;align-items:center;justify-content:center}
</style>
</head>
<body>

<!-- Header -->
<header class="site-header">
  <div class="abs brand">BorrowNest</div>
  <a class="abs btn-outline" href="#appointment">Make an Appointment</a>
  <div class="abs header-phone">
    <svg width="20" height="22" viewBox="0 0 20 22"><path d="M5 2 L8 7 L6 9 C7 12 9 14 12 15 L14 13 L18 16 L16 20 C9 19 3 12 2 5 Z" fill="none" stroke="#0094D4" stroke-width="2" stroke-linejoin="round"/></svg>
    1-800-555-0147
  </div>
  <nav class="abs main-nav">
    <a href="#">Home</a><a href="#">About Us</a><a href="#">Our People</a><a href="#">Loan Options</a><a href="#">Calculators</a><a href="#">Reviews</a><a href="#">Contact Us</a>
  </nav>
</header>

<!-- Hero -->
<section class="hero">
  <div class="abs hero-photo" role="img" aria-label="Photo of a couple meeting a finance broker at a table"></div>
  <div class="abs hero-shade"></div>
  <h1 class="abs hero-title t1">Welcome to</h1>
  <div class="abs hero-title t2">BorrowNest</div>
  <p class="abs hero-sub">We are a finance broking company</p>
  <a class="abs btn-solid hero-btn" href="#">Read More</a>
  <div class="abs dots"><i></i><i></i><i></i><i></i></div>
</section>

<!-- Backdrop shapes behind loan options & about -->
<svg class="abs backdrop" width="1200" height="1292" viewBox="0 0 1200 1292">
  <defs>
    <linearGradient id="bandBlue" x1="0" y1="0" x2="1" y2="0">
      <stop offset="0" stop-color="#3aa6e0"/><stop offset="1" stop-color="#0a7bd0"/>
    </linearGradient>
  </defs>
  <polygon points="0,140 1200,10 1200,-2 0,-2" fill="#fff"/>
  <polygon points="0,140 1200,10 1200,0 0,0" fill="transparent"/>
  <polygon points="0,570 1200,370 1200,1292 0,1292" fill="url(#bandBlue)"/>
</svg>
<svg class="abs" style="left:0;top:860px" width="1200" height="150" viewBox="0 0 1200 150"><polygon points="0,140 1200,10 1200,150 0,150" fill="#fff"/></svg>

<!-- Loan options -->
<section class="abs loan-card">
  <h2 class="section-title">Loan Options</h2>
  <p class="section-lead">Sed ut perspiciatis unde omnis iste natus error sit voluptatem accusantium doloremque laudantium, totam rem aperiam, eaque ipsa quae ab illo inventore veritatis et quasi architecto.</p>
  <div class="abs loan-grid">
    <article class="loan-item is-active">
      <svg width="80" height="72" viewBox="0 0 80 72" fill="none" stroke="#0094D4" stroke-width="2.5"><path d="M8 36 L40 8 L72 36"/><path d="M16 30 V66 H64 V30"/><rect x="32" y="44" width="16" height="22"/><rect x="22" y="34" width="8" height="8"/><rect x="50" y="34" width="8" height="8"/></svg>
      <h3>Home Loans</h3>
      <p>Sed ut perspiciatis unde omnis iste natus error sit voluptatem accusa ntium doloremque.</p>
    </article>
    <article class="loan-item">
      <svg width="80" height="72" viewBox="0 0 80 72" fill="none" stroke="#0094D4" stroke-width="2.5"><path d="M14 36 L22 18 H58 L66 36"/><rect x="8" y="36" width="64" height="18" rx="4"/><circle cx="20" cy="45" r="4"/><circle cx="60" cy="45" r="4"/><path d="M32 45 H48"/><path d="M14 54 V62 H24 V54 M56 54 V62 H66 V54"/></svg>
      <h3>Car Loans</h3>
      <p>Sed ut perspiciatis unde omnis iste natus error sit voluptatem accusa ntium doloremque.</p>
    </article>
    <article class="loan-item">
      <svg width="80" height="72" viewBox="0 0 80 72" fill="none" stroke="#0094D4" stroke-width="2.5"><rect x="10" y="22" width="24" height="44"/><rect x="34" y="6" width="34" height="60"/><path d="M40 14 H46 M54 14 H60 M40 24 H46 M54 24 H60 M40 34 H46 M54 34 H60 M40 44 H46 M54 44 H60 M16 32 H28 M16 42 H28 M16 52 H28"/><path d="M4 66 H76"/></svg>
      <h3>Commercial Loans</h3>
      <p>Sed ut perspiciatis unde omnis iste natus error sit voluptatem accusa ntium doloremque.</p>
    </article>
    <article class="loan-item">
      <svg width="80" height="72" viewBox="0 0 80 72" fill="none" stroke="#0094D4" stroke-width="2.5"><rect x="18" y="8" width="44" height="24" rx="3"/><circle cx="40" cy="20" r="6"/><path d="M6 54 L20 46 H40 L52 52 M6 64 L22 58 H42 L70 44"/></svg>
      <h3>SMSF Loans</h3>
      <p>Sed ut perspiciatis unde omnis iste natus error sit voluptatem accusa ntium doloremque.</p>
    </article>
    <article class="loan-item">
      <svg width="80" height="72" viewBox="0 0 80 72" fill="none" stroke="#0094D4" stroke-width="2.5"><circle cx="30" cy="22" r="14"/><path d="M24 28 L36 16 M25 17 h1 M35 27 h1"/><circle cx="52" cy="36" r="10"/><path d="M52 30 V42 M48 33 H55 M49 39 H56"/><path d="M8 58 L22 50 H40 L48 56 L70 48"/></svg>
      <h3>Business Loans</h3>
      <p>Sed ut perspiciatis unde omnis iste natus error sit voluptatem accusa ntium doloremque.</p>
    </article>
    <article class="loan-item">
      <svg width="80" height="72" viewBox="0 0 80 72" fill="none" stroke="#0094D4" stroke-width="2.5"><rect x="14" y="6" width="42" height="60" rx="2"/><circle cx="35" cy="22" r="7"/><path d="M24 38 H46 M24 46 H46 M24 54 H38"/><path d="M66 20 L50 52 L46 58 L48 50 L64 18 Z"/></svg>
      <h3>Personal Loans</h3>
      <p>Sed ut perspiciatis unde omnis iste natus error sit voluptatem accusa ntium doloremque.</p>
    </article>
  </div>
</section>

<!-- About -->
<section class="about">
  <div class="abs about-photo" role="img" aria-label="Photo of a broker with clients reviewing a laptop"></div>
  <h2 class="abs about-title">About<br>BorrowNest</h2>
  <p class="abs about-text">Sed ut perspiciatis unde omnis iste natus error sit voluptatem accusantium doloremque laudantium, totam rem aperiam, eaque ipsa quae ab illo inventore veritatis et quasi architecto. Nemo enim ipsam voluptatem quia voluptas sit aspernatur aut odit aut fugit, sed quia consequuntur magni dolores eos qui ratione voluptatem sequi nesciunt. Neque porro quisqua.</p>
  <a class="abs btn-solid about-btn" href="#">Read More</a>
</section>

<!-- Our People -->
<section class="people">
  <h2 class="section-title">Our People</h2>
  <p class="section-lead">Sed ut perspiciatis unde omnis iste natus error sit voluptatem accusantium doloremque laudantium, totam rem aperiam, eaque ipsa quae ab illo inventore veritatis et quasi architecto.</p>
  <article class="abs person is-active" style="left:74px">
    <div class="avatar" role="img" aria-label="Team member portrait"></div>
    <h4>Name Heading</h4>
    <p>Sed ut perspiciatis unde omnis iste natus error sit voluptatem accusantium doloremque.</p>
    <svg width="22" height="22" viewBox="0 0 22 22"><circle cx="11" cy="11" r="9" fill="none" stroke="#0094D4" stroke-width="2"/><path d="M6 11 H15 M11 7 L15 11 L11 15" fill="none" stroke="#0094D4" stroke-width="2"/></svg>
  </article>
  <article class="abs person" style="left:344px">
    <div class="avatar" role="img" aria-label="Team member portrait"></div>
    <h4>Name Heading</h4>
    <p>Sed ut perspiciatis unde omnis iste natus error sit voluptatem accusantium doloremque.</p>
    <svg width="22" height="22" viewBox="0 0 22 22"><circle cx="11" cy="11" r="9" fill="none" stroke="#0094D4" stroke-width="2"/><path d="M6 11 H15 M11 7 L15 11 L11 15" fill="none" stroke="#0094D4" stroke-width="2"/></svg>
  </article>
  <article class="abs person" style="left:614px">
    <div class="avatar" role="img" aria-label="Team member portrait"></div>
    <h4>Name Heading</h4>
    <p>Sed ut perspiciatis unde omnis iste natus error sit voluptatem accusantium doloremque.</p>
    <svg width="22" height="22" viewBox="0 0 22 22"><circle cx="11" cy="11" r="9" fill="none" stroke="#0094D4" stroke-width="2"/><path d="M6 11 H15 M11 7 L15 11 L11 15" fill="none" stroke="#0094D4" stroke-width="2"/></svg>
  </article>
  <article class="abs person" style="left:884px">
    <div class="avatar" role="img" aria-label="Team member portrait"></div>
    <h4>Name Heading</h4>
    <p>Sed ut perspiciatis unde omnis iste natus error sit voluptatem accusantium doloremque.</p>
    <svg width="22" height="22" viewBox="0 0 22 22"><circle cx="11" cy="11" r="9" fill="none" stroke="#0094D4" stroke-width="2"/><path d="M6 11 H15 M11 7 L15 11 L11 15" fill="none" stroke="#0094D4" stroke-width="2"/></svg>
  </article>
</section>

<!-- Reviews -->
<section class="abs reviews">
  <h2 class="section-title">Customer Reviews</h2>
  <div class="abs review" style="left:74px">
    <div class="avatar" role="img" aria-label="Customer portrait"></div>
    <div class="stars"><svg width="130" height="20" viewBox="0 0 130 20"><g fill="#ffc515"><path id="st" d="M10 1 L12.6 7 L19 7.4 L14 11.6 L15.6 18 L10 14.4 L4.4 18 L6 11.6 L1 7.4 L7.4 7 Z"/><use href="#st" x="27"/><use href="#st" x="54"/><use href="#st" x="81"/><use href="#st" x="108"/></g></svg></div>
    <h5>Name Heading</h5>
    <p>“ Sed ut perspiciatis unde omnis iste natus error sit voluptatem accusantium doloremque laudantium quasi architecto beatae vitae dicta..”</p>
  </div>
  <div class="abs review" style="left:434px">
    <div class="avatar" role="img" aria-label="Customer portrait"></div>
    <div class="stars"><svg width="130" height="20" viewBox="0 0 130 20"><g fill="#ffc515"><use href="#st"/><use href="#st" x="27"/><use href="#st" x="54"/><use href="#st" x="81"/><use href="#st" x="108"/></g></svg></div>
    <h5>Name Heading</h5>
    <p>“ Sed ut perspiciatis unde omnis iste natus error sit voluptatem accusantium doloremque laudantium quasi architecto beatae vitae dicta..”</p>
  </div>
  <div class="abs review" style="left:794px">
    <div class="avatar" role="img" aria-label="Customer portrait"></div>
    <div class="stars"><svg width="130" height="20" viewBox="0 0 130 20"><g fill="#ffc515"><use href="#st"/><use href="#st" x="27"/><use href="#st" x="54"/><use href="#st" x="81"/><use href="#st" x="108"/></g></svg></div>
    <h5>Name Heading</h5>
    <p>“ Sed ut perspiciatis unde omnis iste natus error sit voluptatem accusantium doloremque laudantium quasi architecto beatae vitae dicta..”</p>
  </div>
</section>

<!-- Steps -->
<section class="steps">
  <h2 class="abs steps-title">Easy to apply. Simple as 1, 2, 3.</h2>
  <svg class="abs" style="left:240px;top:3520px" width="720" height="70" viewBox="0 0 720 70" fill="none" stroke="#555" stroke-width="1.5" stroke-dasharray="4 4">
    <path d="M20 10 C60 70 160 60 220 10"/><path d="M380 10 C420 70 560 60 600 10"/>
  </svg>
  <div class="abs step-btn" style="left:120px">Get Started</div>
  <div class="abs step-num" style="left:219px">1</div>
  <div class="abs step-btn" style="left:480px">Link your Data</div>
  <div class="abs step-num" style="left:579px">2</div>
  <div class="abs step-btn" style="left:840px">Get Funds Fast</div>
  <div class="abs step-num" style="left:939px">3</div>

  <svg class="abs" style="left:200px;top:3612px" width="80" height="80" viewBox="0 0 80 80"><path d="M66 6 C44 6 30 18 22 36 L10 36 L4 48 L18 48 L32 62 L32 76 L44 70 L44 58 C62 50 74 36 74 14 Z" fill="#1c1c1c"/><circle cx="54" cy="26" r="7" fill="#fff"/><path d="M14 58 L6 74 L22 66 Z" fill="#1c1c1c"/></svg>
  <svg class="abs" style="left:560px;top:3612px" width="80" height="80" viewBox="0 0 80 80" fill="none" stroke="#1c1c1c" stroke-width="10" stroke-linecap="round"><path d="M34 46 L24 56 A10 10 0 0 1 10 42 L22 30 A10 10 0 0 1 36 30"/><path d="M46 34 L56 24 A10 10 0 0 1 70 38 L58 50 A10 10 0 0 1 44 50"/><path d="M32 48 L48 32" stroke-width="8"/></svg>
  <svg class="abs" style="left:910px;top:3620px" width="100" height="64" viewBox="0 0 100 64"><rect x="2" y="8" width="96" height="48" fill="#1c1c1c"/><rect x="14" y="18" width="72" height="28" fill="#fff"/><rect x="18" y="22" width="64" height="20" fill="#1c1c1c"/><circle cx="50" cy="32" r="13" fill="#fff"/><path d="M47 25 L51 23 V41" stroke="#1c1c1c" stroke-width="3" fill="none"/></svg>

  <p class="abs step-text" style="left:80px">Sed ut perspiciatis unde omnis iste natus error sit voluptatem.</p>
  <p class="abs step-text" style="left:440px">Sed ut perspiciatis unde omnis iste natus error sit voluptatem.</p>
  <p class="abs step-text" style="left:800px">Sed ut perspiciatis unde omnis iste natus error sit voluptatem.</p>
</section>

<!-- Appointment -->
<section class="abs appointment" id="appointment">
  <h2 class="section-title">Make an Appointment</h2>
  <p class="section-lead">Sed ut perspiciatis unde omnis iste natus error sit voluptatem accusantium doloremque laudatium, totam rem aperiam, eaque ipsa quae ab illo inventore veritatis et quasi.</p>
  <div class="abs field" style="left:162px;top:246px">Name</div>
  <div class="abs field" style="left:614px;top:246px">Email</div>
  <div class="abs field" style="left:162px;top:330px">Phone No</div>
  <div class="abs field" style="left:614px;top:330px">Where do you live?</div>
  <div class="abs field" style="left:162px;top:416px">Subject</div>
  <div class="abs submit" style="left:614px;top:416px">Submit Now</div>
</section>

<!-- Footer -->
<svg class="abs footer-base" width="1200" height="694" viewBox="0 0 1200 694"><polygon points="0,124 1200,0 1200,694 0,694" fill="#111214"/></svg>
<footer class="site-footer">
  <div class="abs brand">BorrowNest</div>
  <div class="abs news-label">Enjoy monthly good business stories &amp; guides</div>
  <div class="abs news-input">Email Address</div>
  <div class="abs news-btn">Subscribe</div>
  <div class="abs footer-rule"></div>

  <div class="abs f-col" style="left:74px;top:4748px">
    <h6>Site Map</h6>
    <ul><li>Home</li><li>About Us</li><li>Our People</li><li>Loan Options</li><li>Calculators</li><li>Reviews</li><li>Contact Us</li></ul>
  </div>
  <div class="abs f-col" style="left:316px;top:4748px">
    <h6>Resources</h6>
    <ul><li>Sed ut perspiciatis</li><li>Unde omnis iste natus</li><li>Error sit voluptatem</li><li>Accusantium dolorem</li><li>Que laudantium</li><li>Sit voluptatem</li></ul>
  </div>
  <div class="abs f-col" style="left:604px;top:4748px">
    <h6>Legal</h6>
    <ul><li>Sed ut perspiciatis</li><li>Unde omnis iste natus</li><li>Error sit voluptatem</li><li>Accusantium dolorem</li><li>Que laudantium</li><li>Sit voluptatem</li></ul>
  </div>
  <div class="abs f-col" style="left:884px;top:4748px">
    <h6>Follow us</h6>
    <div class="socials"><i></i><i></i><i></i><i></i><i></i></div>
    <h6 style="margin-top:34px">Have Question</h6>
    <div class="f-contact"><svg width="18" height="20" viewBox="0 0 20 22"><path d="M5 2 L8 7 L6 9 C7 12 9 14 12 15 L14 13 L18 16 L16 20 C9 19 3 12 2 5 Z" fill="none" stroke="#00A9DD" stroke-width="2"/></svg>1-800-555-0147</div>
    <div class="f-contact"><svg width="22" height="18" viewBox="0 0 22 18"><path d="M2 2 H14 V10 H7 L3 13 V10 H2 Z" fill="#00A9DD"/><path d="M16 6 H20 V14 H19 V17 L15 14 H9 V12 H16 Z" fill="#00A9DD"/></svg>Live Chat</div>
  </div>

  <div class="abs copyright">© Copyright 2022 CompanyName &nbsp;All Rights Reserved</div>
</footer>

</body>
</html>
```